Vormace

I need a professional web site that is directed at the energy industry, Oil, Gas, Mining
I need the website to have the usual pages
1. home page
2. news page.
3. contact us page
4. About us
and a CMS admin section to add further pages and content
Must be Google friendly with SEO facility

Target Market(s)

energy industry, Oil, Gas, Mining

Industry/Entity Type

Industry

Font styles to use
Sans Serif

Colors
faa54b
85cae6
cadf82

Requirements
Must have
• social media icons
site map

```html
<!DOCTYPE html>
<html lang="en">
<head>
<meta charset="utf-8">
<title>Vormace Oil Company</title>
<link href="https://fonts.googleapis.com/css2?family=Source+Sans+3:wght@400;600;700;800&display=swap" rel="stylesheet">
<style>
:root{
  --orange:#f7901e;
  --orange-dark:#d9760f;
  --ink:#1f1f1f;
  --bar:#2b2b2b;
  --brown:#2f1c0c;
  --peach:#fde4c8;
  --card:#fbe6d0;
  --white:#ffffff;
  --muted:#9a9a9a;
}
*{box-sizing:border-box;margin:0;padding:0}
html,body{width:1200px;height:1200px;overflow:hidden;background:var(--white);font-family:"Source Sans 3",Arial,sans-serif;color:var(--ink)}
.page{position:absolute;left:77px;top:43px;width:1035px;height:1127px;background:var(--white);box-shadow:0 0 6px rgba(0,0,0,.35)}
.abs{position:absolute}
.util-bar{left:96px;top:1px;width:845px;height:28px;background:var(--bar);display:flex;justify-content:flex-end;align-items:center;padding-right:50px;gap:12px;font-size:11px;font-weight:600;color:var(--white);letter-spacing:.3px}
.util-bar span.sep{opacity:.9}
.brand{left:124px;top:62px;display:flex;align-items:center;gap:12px;font-size:46px;font-weight:800;letter-spacing:2px;color:var(--ink)}
.brand .mark{width:26px;height:26px;border-radius:50%;background:var(--orange)}
.social-top{left:610px;top:63px;display:flex;gap:10px}
.social-top i{width:37px;height:37px;border-radius:50%;background:#3a3a3a;display:block}
.stay{left:853px;top:60px;width:88px;height:44px;background:var(--bar);color:#ddd;font-size:10px;display:flex;align-items:center;justify-content:center}
.nav{left:0;top:132px;width:1035px;height:51px;background:var(--orange);border-top:7px solid var(--orange-dark)}
.nav ul{list-style:none;position:absolute;left:127px;top:10px;display:flex;gap:8px;font-size:11px;color:var(--white);font-weight:600}
.nav li{padding:6px 13px;border-radius:2px}
.nav li.active{background:#a85a14}
.search{position:absolute;left:619px;top:9px;width:300px;height:25px;background:var(--white);border:2px solid #f5c48c;font-size:13px;color:#b0b0b0;padding:2px 7px}
.search svg{position:absolute;right:10px;top:3px}
.hero{left:96px;top:183px;width:845px;height:380px;background:linear-gradient(180deg,#3b3438 0%,#8a5a3a 30%,#e07a2a 48%,#5a3a26 62%,#241a14 100%)}
.news-panel{left:619px;top:370px;width:322px;height:193px;background:rgba(20,14,10,.82);padding:12px 14px}
.news-panel h2{font-size:22px;font-weight:400;color:var(--orange);margin-bottom:16px}
.news-panel p{font-size:12px;color:var(--white);padding:0 3px 19px;margin-bottom:14px;border-bottom:1px dotted #777}
.news-panel p:last-child{border:0}
.hero-strip{left:96px;top:563px;width:845px;height:55px;background:var(--orange)}
.more{left:619px;top:563px;width:301px;height:55px;background:var(--brown);color:var(--orange);font-size:15px;display:flex;align-items:center;justify-content:center}
.works-title{left:111px;top:634px;font-size:19px;font-weight:400}
.cards{left:104px;top:666px;display:flex;gap:15px}
.card{width:154px;height:152px;background:var(--card);padding:6px}
.card.active{background:var(--orange)}
.card div{width:140px;height:140px}
.connect{left:0;top:832px;width:1035px;height:78px;background:var(--orange);border-top:7px solid var(--orange-dark);text-align:center}
.connect .icons{display:flex;justify-content:center;gap:6px;margin-top:13px}
.connect .icons i{width:24px;height:24px;border-radius:50%;border:2px solid #fde0bf;background:#fbb260;display:block}
.connect p{color:var(--white);font-size:13px;margin-top:7px;letter-spacing:.3px}
.footer{left:0;top:910px;width:1035px;height:217px;background:var(--peach)}
.about{left:129px;top:24px;width:548px}
.about h3{font-size:14px;font-weight:400;padding-bottom:6px;border-bottom:1px dotted #888;margin-bottom:10px}
.about p{font-size:11.4px;line-height:13.8px}
.foot-brand{left:124px;top:150px;font-size:30px;font-weight:800;letter-spacing:1.5px;color:var(--ink);display:flex;align-items:center;gap:8px}
.foot-brand .mark{width:16px;height:16px;border-radius:50%;background:var(--orange)}
.links{left:745px;top:47px;width:189px;border-top:1px dotted #888;padding-top:14px;font-size:10px;line-height:12px;list-style:none}
.links li.gap{margin-top:12px}
</style>
</head>
<body>
<div class="page">
  <div class="abs util-bar"><span>HOME</span><span class="sep">|</span><span>SITE MAP</span><span class="sep">|</span><span>CONTACT US</span></div>
  <div class="abs brand"><span>VORMACE</span><span class="mark"></span></div>
  <div class="abs social-top" aria-label="Social network links"><i></i><i></i><i></i><i></i><i></i></div>
  <div class="abs stay">STAY CONNECTED</div>

  <nav class="abs nav">
    <ul><li class="active">HOME</li><li>ABOUT THE COMPANY</li><li>BUSINESS ACTIVITY</li><li>NEWS</li></ul>
    <div class="search">Search for topics, articles, data...
      <svg width="16" height="16" viewBox="0 0 16 16"><circle cx="6.5" cy="6.5" r="5" fill="none" stroke="#aaa" stroke-width="1.5"/><line x1="10" y1="10" x2="14.5" y2="14.5" stroke="#aaa" stroke-width="1.8"/></svg>
    </div>
  </nav>

  <div class="abs hero" role="img" aria-label="Oil refinery towers at sunset under a dramatic sky"></div>
  <div class="abs news-panel">
    <h2>Latest News</h2>
    <p>Etiam mattis, nibh eu faucibus accumsan</p>
    <p>Quisque dolor quam, tempor in augue quis</p>
    <p>Maecenas nec vestibulum ex</p>
  </div>
  <div class="abs hero-strip"></div>
  <div class="abs more">VIEW MORE NEWS ARTICLES</div>

  <h2 class="abs works-title">See how Vormace Oil Company works</h2>
  <div class="abs cards">
    <div class="card"><div role="img" aria-label="Refinery plant with steel towers" style="background:linear-gradient(180deg,#8fb0d8,#9a9ea4)"></div></div>
    <div class="card active"><div role="img" aria-label="Business team in a meeting" style="background:linear-gradient(135deg,#6a5a4e,#c9a892)"></div></div>
    <div class="card"><div role="img" aria-label="Oil tanker ship at port" style="background:linear-gradient(180deg,#7fa8d8 0%,#b8cbe0 55%,#e76a54 60%,#2f5f86 100%)"></div></div>
    <div class="card"><div role="img" aria-label="Refinery columns against blue sky" style="background:linear-gradient(180deg,#3d6fb0,#8b929a)"></div></div>
    <div class="card"><div role="img" aria-label="Hand refuelling a car" style="background:linear-gradient(135deg,#d8d8d8,#3a3a3a)"></div></div>
  </div>

  <div class="abs connect">
    <div class="icons" aria-label="Social network links"><i></i><i></i><i></i><i></i><i></i></div>
    <p>Connect with us on Social Networks</p>
  </div>

  <footer class="abs footer">
    <div class="abs about">
      <h3>About Vormace Oil Company</h3>
      <p>Lorem ipsum dolor sit amet, consectetur adipiscing elit. Suspendisse in luctus neque. Nam consectetur tempor arcu tempus ultrices. Nulla pellentesque eu urna eget sodales. Nam aliquam augue a magna laoreet vulputate. Ut a dictum eros. Quisque dolor quam, tempor in augue quis, efficitur vestibulum metus. Donec fermentum sem vel arcu imperdiet, sit amet maximus ipsum vulputate. Etiam mattis, nibh eu faucibus accumsan, quam ligula fringilla dolor, non egestas eros libero id ante.</p>
    </div>
    <div class="abs foot-brand"><span>VORMACE</span><span class="mark"></span></div>
    <ul class="abs links">
      <li>Contact Information</li><li>Site Map</li><li>About the Company</li><li>Business Activity</li><li>News</li>
      <li class="gap">Privacy</li><li>Cookies</li><li>Terms</li>
    </ul>
  </footer>
</div>
</body>
</html>
```